National Dance Competition Needs a Program Cover Design

We need a program cover design for our 2017 season programs. Program size is standard 8.5" x 11", full color. The only required elements to include in the design are the Stellar Feet Showcase logo (see uploaded file), and the copy: "2017 Regional Competition" and "20th Anniversary Season". All other design elements are per the creative mind of the designer. Logo can be "embellished" if that's the direction the design leads. This is a children's dance competition (ages 5-19) so design should be colorful, fun, and exciting. The winning design will likely be the springboard to other projects including designs for awards plaques, trophy mylars, and program ads. We are looking to establish an ongoing relationship with a designer. For more information about us go to www.stellarfeetshowcase.com.

Target Market(s)

Dancers ages 5-19, their parents and dance instructors

Requirements
Must have
• See project description above
Should not have
• Do not fall into the mindset that dance is Ballet only. Our kids also compete in Jazz, Tap, Lyrical, Contemporary, Hip Hop and many other styles.

```html
<!DOCTYPE html>
<html lang="en">
<head>
<meta charset="utf-8">
<title>Stellar Feet Showcase – Regional Competition 2017 Program Cover</title>
<link href="https://fonts.googleapis.com/css2?family=Uncial+Antiqua&display=swap" rel="stylesheet">
<style>
  :root {
    --cover-magenta: #b8286e;
    --cover-pink: #e23a68;
    --cover-coral: #ef5a55;
    --cover-orange: #f39a52;
    --badge-navy: #252a3d;
    --title-cream: #e7e5c6;
    --year-teal: #1696b0;
    --logo-ink: #2a1f3e;
    --band-red: rgba(232, 40, 78, 0.82);
    --band-text: #f8dccd;
  }
  html, body {
    margin: 0;
    padding: 0;
    overflow: hidden;
    background: #ffffff;
  }
  .cover {
    position: relative;
    width: 927px;
    height: 1200px;
    overflow: hidden;
    font-family: "Uncial Antiqua", serif;
  }
  .cover-backdrop {
    position: absolute;
    inset: 0;
    background:
      radial-gradient(ellipse at 20% 10%, rgba(120, 30, 90, 0.55), transparent 55%),
      radial-gradient(ellipse at 85% 30%, rgba(110, 60, 130, 0.45), transparent 50%),
      radial-gradient(ellipse at 70% 85%, rgba(250, 170, 90, 0.7), transparent 55%),
      linear-gradient(180deg, var(--cover-magenta) 0%, var(--cover-pink) 40%, var(--cover-coral) 70%, var(--cover-orange) 100%);
  }
  .brand-name {
    position: absolute;
    top: 52px;
    left: 0;
    width: 927px;
    text-align: center;
    margin: 0;
    color: var(--logo-ink);
    font-size: 50px;
    line-height: 1.05;
    font-weight: 400;
  }
  .badge {
    position: absolute;
    left: 0;
    top: 0;
  }
  .band {
    position: absolute;
    height: 82px;
    background: var(--band-red);
    color: var(--band-text);
    font-size: 38px;
    line-height: 82px;
    white-space: nowrap;
  }
  .band-primary {
    left: 0;
    top: 992px;
    width: 424px;
    border-radius: 0 41px 41px 0;
    padding-left: 28px;
    box-sizing: border-box;
  }
  .band-secondary {
    left: 320px;
    top: 1094px;
    width: 607px;
    border-radius: 41px 0 0 41px;
    padding-right: 34px;
    box-sizing: border-box;
    text-align: right;
  }
</style>
</head>
<body>
  <main class="cover">
    <div class="cover-backdrop" role="img" aria-label="Textured abstract background in magenta, pink and orange with soft light rays and glowing constellation lines"></div>

    <h1 class="brand-name">Stellar Feet<br>Showcase</h1>

    <svg class="badge" width="927" height="1200" viewBox="0 0 927 1200" aria-label="Regional Competition 2017">
      <defs>
        <path id="title-arc" d="M 235 520 Q 463 320 692 520"/>
      </defs>
      <circle cx="463" cy="600" r="298" fill="var(--badge-navy)"/>
      <text font-family="Uncial Antiqua, serif" font-size="64" fill="var(--title-cream)" text-anchor="middle">
        <textPath href="#title-arc" startOffset="50%">Regional</textPath>
      </text>
      <text x="463" y="620" font-family="Uncial Antiqua, serif" font-size="66" fill="var(--title-cream)" text-anchor="middle">Competition</text>
      <text x="463" y="795" font-family="Uncial Antiqua, serif" font-size="130" fill="var(--year-teal)" text-anchor="middle">2017</text>
    </svg>

    <div class="band band-primary">20th Anniversary</div>
    <div class="band band-secondary">Season</div>
  </main>
</body>
</html>
```